Brisk Lark Delivery Service Wordpress design

My client is a delivery service whose motto is "We go where the freight leads us." Their colors are red, white and blue. They use Voyara vans and box vans - NO semi tractors. They like this Website design www.kwuzo.com, but I would like to see some designs that make them stand out. Attached is their new logo.

Target Market(s)

Businesses who use delivery services in town and anyone needing freight picked up or transported in the United States.

Industry/Entity Type

Delivery Service

Number of Pages Required

1 page

Font styles to use
Sans Serif

Colors
ec1f27
0455a3
ffffff

Requirements
Must have
• We need a Wordpress design with sliders that incorporates their new logo and the motto "WE GO WHERE THE FREIGHT LEADS US" Their corporate colors are red, white and blue. They only use voyara vans and box vans.
Nice to have
• Please use your creativity to come up with a unique design for this delivery service.
Should not have
• NO SEMI TRACTOR TRAILERS

```html
<!DOCTYPE html>
<html lang="en">
<head>
<meta charset="utf-8">
<title>Brisk Lark Delivery Service</title>
<link rel="stylesheet" href="https://fonts.googleapis.com/css2?family=Oswald:wght@400;500&family=Open+Sans:ital,wght@0,400;0,600;1,400&display=swap">
<style>
:root{
  --red:#ec1f27;
  --blue:#0455a3;
  --blue-soft:#3a74b8;
  --white:#ffffff;
  --ink:#222222;
  --muted:#8a8a8a;
  --line:#dddddd;
  --grey-bg:#ebebeb;
  --dark:#202329;
  --footer:#2a2a2a;
  --footer-text:#9a9a9a;
}
*{box-sizing:border-box;margin:0;padding:0}
html,body{width:1200px;height:3000px;overflow:hidden}
body{position:relative;background:var(--white);font-family:"Open Sans",Arial,sans-serif;color:var(--ink)}
.abs{position:absolute}
.heading{font-family:"Oswald",Arial,sans-serif;font-weight:400;font-size:24px;letter-spacing:.5px;text-transform:uppercase;color:var(--ink);display:flex;align-items:center;gap:22px;white-space:nowrap}
.heading::before,.heading::after{content:"\\\\";color:var(--red);font-size:16px;letter-spacing:-2px;font-style:italic}
.heading.center{left:0;width:100%;justify-content:center}
.btn{position:absolute;background:var(--red);color:var(--white);font-family:"Oswald",Arial,sans-serif;font-size:13px;text-transform:uppercase;display:flex;align-items:center;justify-content:center}
.photo{position:absolute}

/* header */
.header-side{left:0;top:0;width:440px;height:120px;background:var(--grey-bg);clip-path:polygon(0 0,400px 0,440px 120px,0 120px)}
.brand{left:180px;top:40px;display:flex;align-items:center;gap:12px}
.brand-name{font-family:"Oswald",Arial,sans-serif;font-weight:500;font-size:30px;color:var(--blue);text-transform:uppercase;letter-spacing:1px}
.brand-dot{width:34px;height:34px;border-radius:50%;background:var(--red)}
.topbar{left:460px;top:0;width:740px;height:38px;border-bottom:1px solid var(--line);font-size:11px;color:#444}
.login{position:absolute;left:14px;top:12px;display:flex;align-items:center;gap:8px}
.socials{position:absolute;left:398px;top:10px;display:flex;gap:18px}
.socials span{width:14px;height:14px;border-radius:50%;background:#9a9a9a}
.contact-row{top:58px;display:flex;gap:10px;font-size:11px;line-height:15px;color:#333}
.contact-row b{font-weight:600;display:block}
.contact-row small{color:var(--muted);font-size:10.5px}
.nav{left:0;top:120px;width:1200px;height:52px;background:var(--blue)}
.nav a{position:absolute;top:0;height:52px;line-height:52px;color:var(--white);font-family:"Oswald",Arial,sans-serif;font-size:12px;text-transform:uppercase;text-decoration:none}
.nav .active{left:172px;width:90px;background:var(--red);text-align:center;clip-path:polygon(12px 0,100% 0,100% 100%,0 100%)}

/* hero */
.hero{left:0;top:172px;width:1200px;height:430px;background:linear-gradient(100deg,#c9cdd2 0%,#e6e8ea 35%,#cfd2d5 60%,#9ea3a8 100%)}
.motto{left:386px;top:360px;width:540px;height:60px;background:rgba(255,255,255,.72);display:flex;align-items:center;justify-content:center;font-family:"Oswald",Arial,sans-serif;font-size:35px;color:var(--red);text-transform:uppercase}

/* services */
.service{top:692px;width:272px}
.service .photo{left:0;top:0;width:272px;height:180px}
.service .tab{position:absolute;left:0;top:128px;width:84px;height:52px;background:var(--blue);clip-path:polygon(0 0,62px 0,84px 52px,0 52px);display:flex;align-items:center;padding-left:18px}
.service h3{position:absolute;top:202px;font-family:"Oswald",Arial,sans-serif;font-weight:400;font-size:16px;text-transform:uppercase;white-space:nowrap}
.service p{position:absolute;top:244px;width:272px;font-size:11px;line-height:19px;color:var(--muted)}
.service .btn{top:300px;left:0;width:84px;height:32px}

/* quote */
.quote-band{left:0;top:1064px;width:1200px;height:496px;background:var(--blue)}
.quote-photo{left:0;top:1064px;width:620px;height:496px;background:linear-gradient(90deg,#e9e6e1 0%,#d7d3cd 55%,#c8c2b9 100%);clip-path:polygon(0 0,430px 0,440px 0,500px 160px,540px 330px,530px 496px,0 496px)}
.quote-title{left:612px;width:416px;top:1124px;justify-content:center;color:var(--white)}
.quote-title::before,.quote-title::after{color:var(--white)}
.quote-intro{left:612px;top:1186px;width:416px;text-align:center;font-size:11px;line-height:20px;color:#dbe6f3}
.field{position:absolute;border:1px solid #8fb0d6;background:rgba(255,255,255,.08);color:#e3ecf6;font-size:13px;padding:10px 14px}

/* why + news */
.accordion-head{left:172px;width:418px;height:36px;display:flex;align-items:center;font-size:12px;border:1px solid var(--line)}
.accordion-head .ico{width:40px;height:100%;background:var(--red);clip-path:polygon(0 0,28px 0,40px 100%,0 100%);display:flex;align-items:center;padding-left:9px;margin-right:14px}
.accordion-head.open{background:var(--blue);color:var(--white);border-color:var(--blue)}
.accordion-body{left:172px;top:1708px;width:418px;height:132px;border:1px solid var(--line);border-top:none;padding:12px 16px;font-size:11px;line-height:19px;color:var(--muted)}
.news{left:612px;width:416px;height:100px;display:flex;gap:16px}
.news .photo{position:relative;width:90px;height:66px;flex:none}
.news h4{font-size:11.5px;font-weight:600;line-height:16px;margin-top:2px}
.news p{font-size:11px;line-height:17px;color:var(--muted);margin-top:6px}

/* testimonials */
.testimonials{left:0;top:2012px;width:1200px;height:380px;background:var(--dark)}
.testimonials .heading{color:var(--white)}
.quote-card{top:2142px;width:418px;height:118px;background:var(--white);padding:20px 20px;font-style:italic;font-size:12px;line-height:20px;color:var(--muted)}
.quote-card .mark{position:absolute;right:20px;top:78px;color:var(--red);font-family:"Oswald",Arial,sans-serif;font-size:30px;font-style:normal;line-height:1}
.author{top:2236px;width:158px;height:48px;background:var(--blue);color:var(--white);clip-path:polygon(0 0,136px 0,158px 100%,0 100%);padding:8px 18px;font-size:12px;line-height:16px}
.author small{display:block;font-style:italic;font-size:11px}
.dot{top:2334px;width:10px;height:10px;border-radius:50%}

/* clients */
.arrow{top:2452px;width:22px;height:22px;background:var(--blue);display:flex;align-items:center;justify-content:center}
.client{top:2508px;width:124px;height:66px;background:#ececec;display:flex;align-items:center;justify-content:center;font-family:"Open Sans",Arial,sans-serif;font-weight:600;font-size:17px;color:#b5b5b5}

/* footer */
.footer{left:0;top:2618px;width:1200px;height:328px;background:var(--footer)}
.foot-tab{top:2672px;height:36px;padding:0 38px 0 14px;background:var(--blue);color:var(--white);font-family:"Oswald",Arial,sans-serif;font-size:16px;text-transform:uppercase;display:flex;align-items:center;clip-path:polygon(0 0,calc(100% - 18px) 0,100% 100%,0 100%)}
.foot-line{top:2708px;height:1px;background:#3c3c3c}
.foot-list{list-style:none;font-size:11px;line-height:24px;color:var(--footer-text)}
.foot-list li::before{content:"\2192";margin-right:8px;color:#bbb}
.foot-contact{left:756px;top:2742px;font-size:11px;color:var(--footer-text);line-height:16px}
.foot-contact div{display:flex;gap:18px;margin-bottom:14px}
.bottom-bar{left:0;top:2946px;width:1200px;height:54px;background:#1c1c1c}
.copyright{left:0;top:2946px;width:470px;height:54px;background:var(--red);clip-path:polygon(0 0,446px 0,470px 100%,0 100%);color:var(--white);font-size:12px;font-weight:600;display:flex;align-items:center;padding-left:190px}
</style>
</head>
<body>

<!-- header -->
<div class="abs header-side"></div>
<div class="abs brand">
  <span class="brand-name">Brisk Lark</span>
  <span class="brand-dot"></span>
</div>
<div class="abs topbar">
  <div class="login">
    <svg width="11" height="11" viewBox="0 0 12 12"><circle cx="6" cy="3.5" r="3" fill="#555"/><path d="M0 12c0-4 3-5 6-5s6 1 6 5z" fill="#555"/></svg>
    Login / Signup
  </div>
  <div class="socials"><span></span><span></span><span></span><span></span></div>
</div>
<div class="abs contact-row" style="left:470px">
  <svg width="14" height="14" viewBox="0 0 14 14"><path d="M3 1l2.5 3-1.5 1.5c1 2 2.5 3.5 4.5 4.5L10 8.5l3 2.5-1.5 2C6 13 1 8 1 2.5z" fill="var(--red)"/></svg>
  <div><b>+00 000 000 0000</b><small>info@brisklark.com</small></div>
</div>
<div class="abs contact-row" style="left:664px">
  <svg width="12" height="16" viewBox="0 0 12 16"><path d="M6 0a6 6 0 0 1 6 6c0 4-6 10-6 10S0 10 0 6a6 6 0 0 1 6-6z" fill="var(--red)"/><circle cx="6" cy="6" r="2.2" fill="#fff"/></svg>
  <div><b>22 FENWICK LANE</b><small>Ashford, England.</small></div>
</div>
<div class="abs contact-row" style="left:852px">
  <svg width="15" height="15" viewBox="0 0 16 16"><circle cx="8" cy="8" r="6.5" fill="none" stroke="var(--red)" stroke-width="2"/><path d="M8 4v4.5l3 1.5" fill="none" stroke="var(--red)" stroke-width="1.8"/></svg>
  <div><b>MONDAY- SATURDAY 6AM-9PM</b><small>Opening Time</small></div>
</div>

<nav class="abs nav">
  <a class="active" href="#">Home</a>
  <a href="#" style="left:286px">About Us</a>
  <a href="#" style="left:390px">Services</a>
  <a href="#" style="left:488px">News</a>
  <a href="#" style="left:566px">Recruitment</a>
  <a href="#" style="left:692px">Contact Us</a>
  <a href="#" style="left:802px;top:19px;height:14px;line-height:0">
    <svg width="13" height="13" viewBox="0 0 14 14"><circle cx="6" cy="6" r="4.5" fill="none" stroke="#fff" stroke-width="2"/><path d="M9.5 9.5L13 13" stroke="#fff" stroke-width="2"/></svg>
  </a>
</nav>

<!-- hero slider -->
<div class="abs hero" role="img" aria-label="Smiling courier holding a parcel beside a silver delivery van"></div>
<div class="abs motto">We go where the freight leads us</div>

<!-- services -->
<div class="abs heading center" style="top:632px">Our Services</div>

<div class="abs service" style="left:172px">
  <div class="photo" role="img" aria-label="Courier carrying a box outside a building" style="background:linear-gradient(135deg,#d8d2c6,#9a8f80)"></div>
  <div class="tab"><svg width="34" height="20" viewBox="0 0 34 20"><path d="M1 2h20v13H1zM21 6h7l5 5v4H21z" fill="#fff"/><circle cx="8" cy="16" r="3" fill="#fff" stroke="var(--blue)" stroke-width="1.5"/><circle cx="26" cy="16" r="3" fill="#fff" stroke="var(--blue)" stroke-width="1.5"/></svg></div>
  <h3>Quick Service Courier</h3>
  <p>beatae vitae dicta sunt explicabo Tebitis aut rerum necessitatibus saepe repudiandae sint</p>
  <div class="btn">Read More</div>
</div>

<div class="abs service" style="left:466px">
  <div class="photo" role="img" aria-label="Red medical transport cooler box" style="background:linear-gradient(135deg,#c9c5bf,#b3373a)"></div>
  <div class="tab"><svg width="34" height="20" viewBox="0 0 34 20"><path d="M1 3h20v12H1zM21 6h7l5 5v4H21z" fill="#fff"/><path d="M9 6h4v2h2v3h-2v2H9v-2H7V8h2z" fill="var(--blue)"/><circle cx="8" cy="16" r="3" fill="#fff" stroke="var(--blue)" stroke-width="1.5"/><circle cx="26" cy="16" r="3" fill="#fff" stroke="var(--blue)" stroke-width="1.5"/></svg></div>
  <h3>Medical Advantage</h3>
  <p>Teiciendis voluptatibus maiores alias consequatur doloribus asperiores repellat</p>
  <div class="btn">Read More</div>
</div>

<div class="abs service" style="left:758px">
  <div class="photo" role="img" aria-label="Worker unloading large boxes from a van" style="background:linear-gradient(135deg,#aebfa0,#5c6e80)"></div>
  <div class="tab"><svg width="26" height="24" viewBox="0 0 26 24"><path d="M2 1l4 1 4 15h14" fill="none" stroke="#fff" stroke-width="2"/><rect x="11" y="5" width="10" height="9" fill="#fff"/><circle cx="10" cy="20" r="2.5" fill="#fff"/></svg></div>
  <h3>Express Freight</h3>
  <p>Nua dolor sit amet, consectetur adipisci velit sed quia non numquam eius</p>
  <div class="btn">Read More</div>
</div>

<!-- quick quote -->
<div class="abs quote-band"></div>
<div class="abs quote-photo" role="img" aria-label="Smiling delivery man in a cap holding a parcel and clipboard"></div>
<div class="abs heading quote-title">Request a Quick Quote</div>
<p class="abs quote-intro">Nemo enim ipsam voluptatem quia voluptas sit aspernatur aut odit aut fugit sed quia consequuntur magni dolores eos qui ratione voluptatem sequi nesciunt.</p>
<div class="field" style="left:612px;top:1264px;width:202px;height:42px">Name</div>
<div class="field" style="left:822px;top:1264px;width:206px;height:42px">Subject</div>
<div class="field" style="left:612px;top:1314px;width:202px;height:42px">Email</div>
<div class="field" style="left:822px;top:1314px;width:206px;height:42px">Phone</div>
<div class="field" style="left:612px;top:1364px;width:416px;height:82px">Message</div>
<div class="btn" style="left:762px;top:1476px;width:108px;height:38px">Send Message</div>

<!-- why choose us -->
<div class="abs heading" style="left:172px;width:418px;top:1600px;justify-content:center">Why Choose Us</div>
<div class="abs accordion-head open" style="top:1672px">
  <span class="ico"><svg width="12" height="12" viewBox="0 0 12 12"><path d="M6 1v9M2 6l4 4 4-4" fill="none" stroke="#fff" stroke-width="2"/></svg></span>Specialised Fleet Management Services
</div>
<div class="abs accordion-body">Itaque earum rerum hic tenetur a sapiente delectus, ut aut reiciendis voluptatibus maiores alias consequatur aut perferendis doloribus asperiores repellat. Temporibus autem quibusdam et aut officiis debitis aut rerum necessitatibus saepe eveniet ut et voluptates repudiandae sint et molestiae non recusandae.</div>
<div class="abs accordion-head" style="top:1844px">
  <span class="ico"><svg width="12" height="12" viewBox="0 0 12 12"><path d="M1 6h9M6 2l4 4-4 4" fill="none" stroke="#fff" stroke-width="2"/></svg></span>Family Run Business (20 years)
</div>
<div class="abs accordion-head" style="top:1886px">
  <span class="ico"><svg width="12" height="12" viewBox="0 0 12 12"><path d="M1 6h9M6 2l4 4-4 4" fill="none" stroke="#fff" stroke-width="2"/></svg></span>Driver Support
</div>
<div class="abs accordion-head" style="top:1928px">
  <span class="ico"><svg width="12" height="12" viewBox="0 0 12 12"><path d="M1 6h9M6 2l4 4-4 4" fill="none" stroke="#fff" stroke-width="2"/></svg></span>Cost Effective
</div>

<!-- latest news -->
<div class="abs heading" style="left:612px;width:416px;top:1600px;justify-content:center">Latest News</div>
<div class="abs news" style="top:1676px;border-bottom:1px solid var(--line)">
  <div class="photo" role="img" aria-label="White delivery van on the road" style="background:linear-gradient(135deg,#d7dadd,#8e9399)"></div>
  <div><h4>Duis aute irure dolor in reprehenderit in voluptate</h4><p>Lorem ipsum dolor sit amet, consectetur adipiscing elit, sed do eiusmod tempor incididunt ut labore.</p></div>
</div>
<div class="abs news" style="top:1788px;border-bottom:1px solid var(--line)">
  <div class="photo" role="img" aria-label="Courier stacking parcels" style="background:linear-gradient(135deg,#c9a882,#7a5c44)"></div>
  <div><h4>Nemo enim ipsam voluptatem quia voluptas sit</h4><p>Eus modi tempora incidunt ut labore et dolore magnam aliquam quaerat voluptatem.</p></div>
</div>
<div class="abs news" style="top:1900px">
  <div class="photo" role="img" aria-label="Driver at the wheel of a van" style="background:linear-gradient(135deg,#c4c6c8,#55585c)"></div>
  <div><h4>Quam nihil molestiae consequatur vel illum qui</h4><p>Magni dolores eos qui ratione voluptatem sequi nesciunt. Neque porro quisquam est.</p></div>
</div>

<!-- testimonials -->
<div class="abs testimonials"></div>
<div class="abs heading center" style="top:2068px;color:var(--white)">Testimonials</div>
<div class="abs quote-card" style="left:172px">Quis autem vel eum iure reprehenderit qui in ea voluptate velit esse quam nihil molestiae consequatur<span class="mark">&ldquo;</span></div>
<div class="abs author" style="left:172px">Dale Porter<small>CEO Haulway Ltd.</small></div>
<div class="abs quote-card" style="left:612px;background:#f1f0ee">Accusamus et iusto odio dignissimos ducimus qui blanditiis praesentium voluptatum deleniti atque<span class="mark">&ldquo;</span></div>
<div class="abs author" style="left:612px">Ruth Calder<small>CEO Haulway Ltd.</small></div>
<div class="abs dot" style="left:584px;background:var(--white)"></div>
<div class="abs dot" style="left:598px;background:#777"></div>

<!-- clients -->
<div class="abs heading center" style="top:2430px">Our Clients</div>
<div class="abs arrow" style="left:980px"><svg width="8" height="10" viewBox="0 0 8 10"><path d="M6 1L2 5l4 4" fill="none" stroke="#fff" stroke-width="2"/></svg></div>
<div class="abs arrow" style="left:1006px"><svg width="8" height="10" viewBox="0 0 8 10"><path d="M2 1l4 4-4 4" fill="none" stroke="#fff" stroke-width="2"/></svg></div>
<div class="abs client" style="left:172px">Mabels</div>
<div class="abs client" style="left:318px">Nooda</div>
<div class="abs client" style="left:464px">Greenfold</div>
<div class="abs client" style="left:612px">Crumbly</div>
<div class="abs client" style="left:758px">Wrenby</div>
<div class="abs client" style="left:904px">Perch</div>

<!-- footer -->
<footer class="abs footer"></footer>
<div class="abs foot-tab" style="left:172px">About Us</div>
<div class="abs foot-line" style="left:172px;width:270px"></div>
<div class="abs" style="left:172px;top:2740px;font-family:'Oswald',Arial,sans-serif;font-size:20px;color:#8d8d8d;text-transform:uppercase;letter-spacing:1px">Brisk Lark</div>
<p class="abs" style="left:172px;top:2800px;width:280px;font-size:11px;line-height:19px;color:var(--footer-text)">Duis aute irure dolor in reprehenderit in voluptate velit esse cillum dolore eu fugiat nulla pariatur</p>

<div class="abs foot-tab" style="left:466px">Information</div>
<div class="abs foot-line" style="left:466px;width:270px"></div>
<ul class="abs foot-list" style="left:466px;top:2740px">
  <li>About Us</li><li>Services</li><li>Recruitment</li><li>News</li><li>Contact</li>
</ul>
<ul class="abs foot-list" style="left:598px;top:2740px">
  <li>Driver Support</li><li>Fuel Management</li><li>Terms &amp; Condition</li><li>Support Details</li>
</ul>

<div class="abs foot-tab" style="left:756px">Contact Us</div>
<div class="abs foot-line" style="left:756px;width:272px"></div>
<div class="abs foot-contact">
  <div><svg width="10" height="14" viewBox="0 0 12 16"><path d="M6 0a6 6 0 0 1 6 6c0 4-6 10-6 10S0 10 0 6a6 6 0 0 1 6-6z" fill="#bbb"/></svg><span>22 Fenwick Lane<br>Ashford, England.</span></div>
  <div><svg width="12" height="12" viewBox="0 0 14 14"><path d="M3 1l2.5 3-1.5 1.5c1 2 2.5 3.5 4.5 4.5L10 8.5l3 2.5-1.5 2C6 13 1 8 1 2.5z" fill="#bbb"/></svg><span>+0 000 000 0000</span></div>
  <div><svg width="12" height="12" viewBox="0 0 12 12"><rect x="1" y="4" width="10" height="7" fill="#bbb"/><rect x="3" y="1" width="6" height="3" fill="#bbb"/></svg><span>+0 000 000 0000</span></div>
  <div><svg width="12" height="10" viewBox="0 0 12 10"><rect x="0" y="0" width="12" height="10" fill="#bbb"/><path d="M0 0l6 5 6-5" fill="none" stroke="#2a2a2a" stroke-width="1.2"/></svg><span>info@brisklark.com</span></div>
</div>

<div class="abs bottom-bar"></div>
<div class="abs copyright">&copy; Copyright information here</div>

</body>
</html>
```